Flyer for Mountain Bike Skills Event

Create an 11x17 posts for an upcoming Mountain Bike Skills event.

Falcon Trail Riding Academy Logo
--
Are you ready to ride your mountain bike faster and with more confidence? Join us to learn how to take your riding to the next level!
--
EVENT INFORMATION:

Saturday April 23
>> Fundamental Skills Clinic
>> Jumping Mini Clinic

Sunday April 24
>> Intermediate / Advanced Skills Clinic

Saturday - Sunday April 23/24
>> 2 Day Skills Camp

--
San Diego, California
--
Following your clinic, you will see an immediate improvement in your riding and a boost in confidence.

Skills taught and practiced in courses include:

Mind skills
Mastering manual front-wheel lifts
Manual dropping roots & steps
Cornering with speed & confidence
Reading & breaking down the trail
Introduction to energy management & flow
Linking trail sections for flow
Attacking flat corners
Flat and cambered corners
Bermed corners; lines and pumping
Switchbacks
Maximizing grip and traction with pumping
Learning to pump for speed & air

Event hosted by: HARLOWE CYCLE WORKS (*use logo)

Sign up today!
--
More informaiton on our website:
WWW.PEDALWITHAFALCON.COM

Target Market(s)

Mountain bikers age 35-60

Industry/Entity Type

Fitness

Requirements
Must have
• Falcon Logo
• Should be consistent with the Falcon brand, see website for examples: https://coastaltrailcraftlessons.com/ and our truck wrap design file.
• Flyer needs to be easy to read and include all the content in the project description.
Nice to have
• Include our tag line: PEDAL WITH A FALCON

```html
<!DOCTYPE html>
<html lang="en">
<head>
<meta charset="utf-8">
<title>Falcon Trail Riding Academy – Skills Clinic Flyer</title>
<link rel="stylesheet" href="https://fonts.googleapis.com/css2?family=Roboto+Condensed:ital,wght@0,400;0,700;1,400;1,700;1,900&display=swap">
<style>
  :root {
    --forest-dark: #1f2a17;
    --forest-mid: #3f5a2a;
    --forest-light: #6f8a45;
    --panel: rgba(40, 40, 40, 0.92);
    --ink: #111111;
    --orange: #f26a1b;
    --red-orange: #e8411c;
    --yellow: #f7e11b;
    --white: #ffffff;
  }
  * { box-sizing: border-box; margin: 0; padding: 0; }
  html, body { width: 778px; height: 1200px; overflow: hidden; background: #000; }
  body { font-family: "Roboto Condensed", sans-serif; color: var(--white); }

  .flyer { position: relative; width: 778px; height: 1200px; overflow: hidden; }

  .backdrop {
    position: absolute; inset: 0;
    background:
      radial-gradient(ellipse at 75% 15%, #8fa65a 0%, transparent 45%),
      linear-gradient(160deg, var(--forest-light) 0%, var(--forest-mid) 40%, var(--forest-dark) 100%);
  }

  .brand {
    position: absolute; left: 0; top: 0; width: 300px; height: 140px;
    background: var(--white); color: var(--ink);
    display: flex; align-items: center; gap: 14px; padding: 0 18px;
  }
  .brand-dot { width: 26px; height: 26px; border-radius: 50%; background: var(--ink); flex: none; }
  .brand-name { font-weight: 700; font-size: 27px; line-height: 1.05; text-transform: uppercase; }

  .headline {
    position: absolute; left: -10px; top: 262px; width: 800px;
    transform: rotate(-5deg); transform-origin: left top;
    background: rgba(0,0,0,0.6); padding: 10px 40px;
    font-weight: 900; font-style: italic; font-size: 40px; line-height: 1.08;
    color: var(--red-orange); text-align: center;
  }

  .invite {
    position: absolute; left: 95px; top: 415px; width: 660px;
    transform: rotate(-5deg); transform-origin: left top;
    font-weight: 700; font-style: italic; font-size: 37px; line-height: 1.12;
    color: var(--white); text-align: center; text-shadow: 0 2px 4px rgba(0,0,0,0.6);
  }

  .skills {
    position: absolute; left: 0; top: 545px; width: 390px; height: 525px;
    background: var(--panel); padding: 30px 16px 0 22px;
  }
  .skills-title { color: var(--yellow); font-weight: 700; font-size: 21px; line-height: 1.2; margin-bottom: 8px; }
  .skills-list { list-style: none; font-size: 18px; line-height: 28px; white-space: nowrap; }
  .skills-list li::before { content: "• "; }

  .info {
    position: absolute; left: 405px; top: 545px; width: 360px;
    display: flex; flex-direction: column;
  }
  .day {
    align-self: flex-start; background: var(--orange); color: var(--white);
    font-weight: 700; font-size: 23px; line-height: 34px; padding: 0 10px; margin-top: 8px;
  }
  .sessions { list-style: none; background: rgba(0,0,0,0.75); padding: 3px 10px; font-size: 19px; line-height: 27px; }
  .sessions li::before { content: "\25C6  "; color: var(--orange); font-size: 14px; }

  .promise {
    margin-top: 16px;
    font-style: italic; font-weight: 700; font-size: 20px; line-height: 1.25;
  }

  .host {
    margin-top: 12px; align-self: flex-end;
    display: flex; align-items: center; gap: 12px;
  }
  .host-text { text-align: right; font-weight: 700; font-size: 17px; line-height: 1.2; }
  .host-label { font-style: italic; font-weight: 400; display: block; }
  .host-mark { width: 58px; height: 58px; border-radius: 50%; background: var(--white); flex: none; }

  .cta {
    position: absolute; left: 0; right: 0; top: 1075px; text-align: center;
    font-weight: 900; font-style: italic; font-size: 54px; line-height: 62px; color: var(--yellow);
    text-shadow: 0 3px 6px rgba(0,0,0,0.6);
  }
  .website {
    position: absolute; left: 0; right: 0; top: 1145px; text-align: center;
    font-weight: 700; font-size: 24px; letter-spacing: 0.5px;
  }
</style>
</head>
<body>
<main class="flyer">
  <div class="backdrop" role="img" aria-label="Photo of a mountain biker riding through a green forest trail"></div>

  <header class="brand">
    <span class="brand-dot"></span>
    <span class="brand-name">Falcon Trail Riding Academy</span>
  </header>

  <h1 class="headline">Are you ready to ride your mountain bike faster and with more confidence?</h1>
  <p class="invite">Join us to learn how to take your riding to the next level!</p>

  <section class="skills">
    <h2 class="skills-title">Skills taught and practiced<br>in courses include:</h2>
    <ul class="skills-list">
      <li>Mind skills</li>
      <li>Mastering manual front-wheel lifts</li>
      <li>Manual dropping roots &amp; steps</li>
      <li>Cornering with speed &amp; confidence</li>
      <li>Reading &amp; breaking down the trail</li>
      <li>Introduction to energy management &amp; flow</li>
      <li>Linking trail sections for flow</li>
      <li>Attacking flat corners</li>
      <li>Flat and cambered corners</li>
      <li>Bermed corners; lines and pumping</li>
      <li>Switchbacks</li>
      <li>Maximizing grip and traction with pumping</li>
      <li>Learning to pump for speed &amp; air</li>
    </ul>
  </section>

  <section class="info">
    <div class="day">Saturday April 23</div>
    <ul class="sessions"><li>Fundamental Skills Clinic</li><li>Jumping Mini Clinic</li></ul>
    <div class="day">Sunday April 24</div>
    <ul class="sessions"><li>Intermediate / Advanced Skills Clinic</li></ul>
    <div class="day">Saturday - Sunday April 23/24</div>
    <ul class="sessions"><li>2 Day Skills Camp</li></ul>
    <div class="day">Sunday April 24</div>
    <ul class="sessions"><li>San Diego, California</li></ul>

    <p class="promise">Following your clinic, you will see an immediate improvement in your riding and a boost in confidence.</p>

    <div class="host">
      <p class="host-text"><span class="host-label">Hosted by</span>HARLOWE CYCLE WORKS</p>
      <span class="host-mark"></span>
    </div>
  </section>

  <p class="cta">SIGN UP TODAY!</p>
  <p class="website">WWW.PEDALWITHAFALCON.COM</p>
</main>
</body>
</html>
```